The Quiet Ledger Method - Seven Weekend Fixes

Nonfiction book about how to save on insurance. Almost one hundred measures and examples to reduce ones insurance costs.

Target Market(s)

Men/Women between 18 and 50

Industry/Entity Type

Insurance

```html
<!DOCTYPE html>
<html lang="en">
<head>
<meta charset="utf-8">
<title>The Quiet Ledger Method – Book Cover</title>
<link rel="stylesheet" href="https://fonts.googleapis.com/css2?family=Alfa+Slab+One&family=Open+Sans:wght@800&display=swap">
<style>
  :root {
    --page-bg: #f2f2f2;
    --cover-bg: #ffffff;
    --cover-edge: #e2e2e2;
    --ink: #111111;
    --accent-red: #e3222b;
    --accent-red-dark: #b9161e;
    --band-text: #ffffff;
    --art-light: #f4f4f4;
    --art-warm: #f3ddd0;
  }
  * { margin: 0; padding: 0; box-sizing: border-box; }
  html, body {
    width: 809px;
    height: 1200px;
    overflow: hidden;
    background: var(--page-bg);
  }
  .canvas {
    position: relative;
    width: 809px;
    height: 1200px;
  }
  .cover {
    position: absolute;
    left: 104px;
    top: 150px;
    width: 600px;
    height: 900px;
    background: var(--cover-bg);
    border: 1px solid var(--cover-edge);
    overflow: hidden;
  }
  .title {
    position: absolute;
    top: 34px;
    left: 0;
    width: 100%;
    text-align: center;
    font-family: "Alfa Slab One", serif;
    font-weight: 400;
    color: var(--ink);
    line-height: 0.95;
    text-transform: uppercase;
  }
  .title__lead { display: block; font-size: 82px; }
  .title__key { display: block; font-size: 128px; color: var(--accent-red); margin-top: 2px; }
  .title__tail { display: block; font-size: 78px; margin-top: 2px; }
  .subtitle-band {
    position: absolute;
    top: 340px;
    left: 0;
    width: 100%;
    height: 62px;
    background: linear-gradient(to right, var(--accent-red-dark), var(--accent-red) 55%, var(--accent-red-dark));
    display: flex;
    align-items: center;
    justify-content: center;
    font-family: "Open Sans", sans-serif;
    font-weight: 800;
    font-size: 34px;
    letter-spacing: 0.5px;
    color: var(--band-text);
    text-transform: uppercase;
  }
  .cover-illustration {
    position: absolute;
    top: 432px;
    left: 70px;
    width: 460px;
    height: 300px;
    background: linear-gradient(180deg, var(--art-light) 0%, var(--art-warm) 100%);
  }
  .author {
    position: absolute;
    top: 770px;
    left: 0;
    width: 100%;
    text-align: center;
    font-family: "Alfa Slab One", serif;
    font-weight: 400;
    font-size: 40px;
    color: var(--ink);
    text-transform: uppercase;
  }
</style>
</head>
<body>
  <main class="canvas">
    <article class="cover">
      <h1 class="title">
        <span class="title__lead">The Quiet</span>
        <span class="title__key">Ledger</span>
        <span class="title__tail">Method</span>
      </h1>
      <p class="subtitle-band">Seven Weekend Fixes</p>
      <div class="cover-illustration" role="img" aria-label="Cover illustration: a stopwatch resting in a life ring"></div>
      <p class="author">Author Name</p>
    </article>
  </main>
</body>
</html>
```